Stationery including letterhead, business cards, for a new Chartered Accounting Practice

I need a new set of stationery including letterhead, business cards, for a new Chartered Accounting Practice based in Melbourne, Victoria, Australia called "Brint Holloway, Chartered Accountant".

I will be providing Auditing and general consulting advice to small and medium business enterprises. The final design should communicate trust, wisdom and security.

Target Market(s)

Target Market English speaking, Australians. Proprietors small and medium sized businesses - aged 45-65. Fellow professionals - lawyers, investment consultants, other accountants. Retirees - aged 60 and over

Industry/Entity Type

Accountant

Font styles to use
Serif

Colors
0355a3

Requirements
Must have
• The final design should convey trust, wisdom and security.
• Names of practice "Brint Holloway , Chartered Accountant"
• Contact details:
• Address 284 Marbury Street, Tallow Creek, Victoria, 3172, Australia
• Telephone: 047 000 3158
• Email: brintholloway@postquill.example
Nice to have
• an expensive and professional design, the letterhead should be timeless with a logo on white space
Should not have
• no bright/fluro colours

```html
<!DOCTYPE html>
<html lang="en">
<head>
<meta charset="utf-8">
<title>Brint Holloway, Chartered Accountant — Letterhead</title>
<link rel="stylesheet" href="https://fonts.googleapis.com/css2?family=Montserrat:wght@300;500&family=Open+Sans:wght@400&display=swap">
<style>
  :root {
    --backdrop: #6b9ea1;
    --paper: #ffffff;
    --sky-blue: #0a8fd0;
    --navy: #0355a3;
    --charcoal: #3a3f46;
    --ink: #2b2f35;
    --white: #ffffff;
  }
  html, body {
    margin: 0;
    padding: 0;
    width: 1200px;
    height: 800px;
    overflow: hidden;
    background: var(--backdrop);
  }
  .canvas {
    position: relative;
    width: 1200px;
    height: 800px;
  }
  .letterhead {
    position: absolute;
    left: 343px;
    top: 38px;
    width: 513px;
    height: 725px;
    background: var(--paper);
    box-shadow: 0 6px 24px rgba(0, 0, 0, 0.18);
  }
  .header-band {
    position: absolute;
    left: 0;
    top: 41px;
    width: 240px;
    height: 138px;
    background: var(--charcoal);
    border-top: 10px solid var(--navy);
    border-bottom: 10px solid var(--navy);
    box-sizing: border-box;
  }
  .header-rule {
    position: absolute;
    left: 0;
    top: 183px;
    width: 240px;
    height: 3px;
    background: var(--sky-blue);
  }
  .practice-lockup {
    position: absolute;
    left: 0;
    top: 0;
    width: 240px;
    height: 118px;
    display: flex;
    flex-direction: column;
    justify-content: center;
    align-items: center;
    color: var(--white);
    font-family: "Montserrat", sans-serif;
  }
  .practice-name {
    margin: 0;
    font-size: 17px;
    font-weight: 500;
    letter-spacing: 0.2px;
    line-height: 1.1;
  }
  .practice-title {
    margin: 5px 0 0;
    font-size: 10.5px;
    font-weight: 300;
    letter-spacing: 0.3px;
    line-height: 1;
  }
  .contact-bar {
    position: absolute;
    left: 42px;
    right: 22px;
    top: 657px;
    display: flex;
    justify-content: space-between;
    align-items: center;
    font-family: "Open Sans", sans-serif;
    color: var(--ink);
  }
  .contact-item {
    display: flex;
    align-items: center;
    white-space: nowrap;
  }
  .contact-phone { font-size: 10.5px; }
  .contact-email { font-size: 8px; }
  .contact-address { font-size: 8px; line-height: 1.3; }
  .contact-icon {
    width: 18px;
    height: 18px;
    margin-right: 7px;
    flex: none;
  }
</style>
</head>
<body>
<main class="canvas">
  <article class="letterhead">
    <header class="header-band">
      <div class="practice-lockup">
        <h1 class="practice-name">BRINT HOLLOWAY</h1>
        <p class="practice-title">CHARTERED ACCOUNTANT</p>
      </div>
    </header>
    <div class="header-rule"></div>

    <footer class="contact-bar">
      <div class="contact-item contact-phone">
        <svg class="contact-icon" viewBox="0 0 22 22" aria-hidden="true">
          <rect width="22" height="22" fill="var(--sky-blue)"/>
          <path d="M7.5 5.5 L9.5 5.5 L10.3 8.5 L9 9.6 C9.8 11.3 10.9 12.4 12.5 13.1 L13.6 11.8 L16.5 12.6 L16.5 14.6 C16.5 15.4 15.8 16 15 15.9 C10.5 15.4 6.7 11.6 6.1 7 C6 6.2 6.7 5.5 7.5 5.5 Z" fill="var(--white)"/>
        </svg>
        <span>047 000 3158</span>
      </div>
      <div class="contact-item contact-email">
        <svg class="contact-icon" viewBox="0 0 22 22" aria-hidden="true">
          <rect width="22" height="22" fill="var(--sky-blue)"/>
          <g fill="none" stroke="var(--white)" stroke-width="1.1">
            <circle cx="11" cy="11" r="5.5"/>
            <ellipse cx="11" cy="11" rx="2.4" ry="5.5"/>
            <line x1="5.5" y1="11" x2="16.5" y2="11"/>
          </g>
        </svg>
        <span>brintholloway@postquill.example</span>
      </div>
      <div class="contact-item contact-address">
        <svg class="contact-icon" viewBox="0 0 22 22" aria-hidden="true">
          <rect width="22" height="22" fill="var(--charcoal)"/>
          <path d="M11 4.8 C8.5 4.8 6.8 6.6 6.8 8.9 C6.8 11.9 11 16.8 11 16.8 C11 16.8 15.2 11.9 15.2 8.9 C15.2 6.6 13.5 4.8 11 4.8 Z" fill="none" stroke="var(--white)" stroke-width="1.3"/>
          <circle cx="11" cy="9" r="1.6" fill="var(--white)"/>
        </svg>
        <span>284 Marbury Street, Tallow Creek<br>Victoria, 3172, Australia</span>
      </div>
    </footer>
  </article>
</main>
</body>
</html>
```